Vornfield Business Cards

Logo files are included. Full "Vornfield" logo should be included on the back of the business card. The H symbol should be included on the front with the contact information.

Vornfield, LLC is the company name and we do commercial construction and real estate development consulting services. Look for a fairly simple card design utilizing our logo.

```html
<!DOCTYPE html>
<html lang="en">
<head>
<meta charset="utf-8">
<title>Vornfield Business Cards</title>
<link rel="stylesheet" href="https://fonts.googleapis.com/css2?family=Montserrat:wght@500;600;700&family=Playfair+Display:wght@800&family=Libre+Baskerville&display=swap">
<style>
  :root {
    --navy: #1b374d;
    --gold: #e9a923;
    --white: #ffffff;
    --ink: #1c1c1c;
    --backdrop: #e9ebee;
    --rule: #555a60;
  }
  * { box-sizing: border-box; margin: 0; padding: 0; }
  html, body { width: 1200px; height: 1200px; overflow: hidden; }
  body {
    background: var(--backdrop);
    font-family: "Montserrat", sans-serif;
    display: flex;
    flex-direction: column;
    align-items: center;
    justify-content: center;
    gap: 80px;
  }
  .card {
    position: relative;
    width: 760px;
    height: 434px;
    background: var(--white);
    overflow: hidden;
    box-shadow: 0 6px 24px rgba(0,0,0,0.12);
  }
  .band {
    position: absolute;
    left: 0; right: 0; bottom: 0;
    background: var(--navy);
  }

  /* Back */
  .card-back .band { height: 120px; }
  .brand {
    position: absolute;
    top: 108px; left: 0; right: 0;
    display: flex;
    flex-direction: column;
    align-items: center;
    gap: 18px;
  }
  .brand-dot {
    width: 54px; height: 54px;
    border-radius: 50%;
    background: var(--gold);
  }
  .brand-name {
    font-weight: 600;
    font-size: 62px;
    letter-spacing: 4px;
    color: var(--navy);
    text-transform: uppercase;
    line-height: 1;
  }
  .web-tag {
    position: absolute;
    left: 250px; top: 284px;
    width: 300px; height: 60px;
  }
  .web-tag span {
    position: absolute;
    inset: 0;
    display: flex; align-items: center; justify-content: center;
    font-weight: 700;
    font-size: 18px;
    letter-spacing: 2px;
    color: var(--white);
  }

  /* Front */
  .card-front .band { height: 110px; }
  .person {
    position: absolute;
    left: 120px; top: 170px;
  }
  .person-name {
    font-family: "Playfair Display", serif;
    font-weight: 800;
    font-size: 46px;
    color: var(--navy);
    line-height: 1.05;
  }
  .person-role {
    font-family: "Libre Baskerville", serif;
    font-size: 17px;
    color: var(--gold);
    margin-top: 6px;
  }
  .divider {
    position: absolute;
    left: 430px; top: 90px;
    width: 1px; height: 150px;
    background: var(--rule);
  }
  .contacts {
    position: absolute;
    left: 470px; top: 92px;
    list-style: none;
    display: flex; flex-direction: column; gap: 12px;
  }
  .contacts li {
    display: flex; align-items: center; gap: 18px;
    font-size: 17px;
    font-weight: 500;
    color: var(--ink);
  }
  .contacts svg { width: 16px; height: 16px; fill: var(--gold); flex: none; }
  .front-brand {
    position: absolute;
    left: 470px; top: 272px;
    display: flex; align-items: center; gap: 10px;
  }
  .front-brand .brand-dot { width: 22px; height: 22px; }
  .front-brand .brand-name { font-size: 26px; letter-spacing: 2px; }
  .address {
    position: absolute;
    left: 0; right: 0; bottom: 0; height: 110px;
    display: flex; align-items: center; justify-content: center;
    font-weight: 700;
    font-size: 19px;
    letter-spacing: 2.5px;
    color: var(--white);
    text-transform: uppercase;
  }
</style>
</head>
<body>

  <section class="card card-back" aria-label="Card back">
    <div class="band"></div>
    <div class="brand">
      <div class="brand-dot"></div>
      <div class="brand-name">Vornfield</div>
    </div>
    <div class="web-tag">
      <svg viewBox="0 0 300 60" width="300" height="60" aria-hidden="true">
        <polygon points="14,0 286,0 300,16 300,44 286,60 14,60 0,44 0,16" fill="var(--gold)"/>
      </svg>
      <span>WWW.VORNFIELD.COM</span>
    </div>
  </section>

  <section class="card card-front" aria-label="Card front">
    <div class="band"></div>
    <div class="person">
      <div class="person-name">Lena Marwick</div>
      <div class="person-role">Founder &amp; Business Head</div>
    </div>
    <div class="divider"></div>
    <ul class="contacts">
      <li>
        <svg viewBox="0 0 24 24" aria-hidden="true"><path d="M6.6 10.8a15 15 0 0 0 6.6 6.6l2.2-2.2c.3-.3.7-.4 1-.2 1.1.4 2.3.6 3.6.6.6 0 1 .4 1 1V20c0 .6-.4 1-1 1A17 17 0 0 1 3 4c0-.6.4-1 1-1h3.5c.6 0 1 .4 1 1 0 1.3.2 2.5.6 3.6.1.3 0 .7-.2 1z"/></svg>
        +1 415 555 0187
      </li>
      <li>
        <svg viewBox="0 0 24 24" aria-hidden="true"><path d="M6 2h9v6H6zM4 9h16v13H4zm3 3v2h2v-2zm4 0v2h2v-2zm4 0v2h2v-2zm-8 4v2h2v-2zm4 0v2h2v-2zm4 0v2h2v-2z"/></svg>
        +1 415 555 0188
      </li>
      <li>
        <svg viewBox="0 0 24 24" aria-hidden="true"><path d="M2 5h20v14H2zm2 2v.5l8 5 8-5V7l-8 5z"/></svg>
        hello@vornfield.com
      </li>
      <li>
        <svg viewBox="0 0 24 24" aria-hidden="true"><path d="M12 2a10 10 0 1 0 0 20 10 10 0 0 0 0-20zm6.9 6h-3a15 15 0 0 0-1.3-3.9A8 8 0 0 1 18.9 8zM12 4c.8 1.2 1.5 2.5 1.9 4h-3.8c.4-1.5 1.1-2.8 1.9-4zM4.3 14a8 8 0 0 1 0-4h3.4a16 16 0 0 0 0 4zm.8 2h3a15 15 0 0 0 1.3 3.9A8 8 0 0 1 5.1 16zm3-8h-3a8 8 0 0 1 4.3-3.9A15 15 0 0 0 8.1 8zM12 20c-.8-1.2-1.5-2.5-1.9-4h3.8c-.4 1.5-1.1 2.8-1.9 4zm2.3-6H9.7a14 14 0 0 1 0-4h4.6a14 14 0 0 1 0 4zm.3 5.9c.6-1.2 1-2.5 1.3-3.9h3a8 8 0 0 1-4.3 3.9zm1.7-5.9a16 16 0 0 0 0-4h3.4a8 8 0 0 1 0 4z"/></svg>
        www.vornfield.com
      </li>
    </ul>
    <div class="front-brand">
      <div class="brand-dot"></div>
      <div class="brand-name">Vornfield</div>
    </div>
    <div class="address">27 Alder Crescent Road, Fairhaven, CA 90418</div>
  </section>

</body>
</html>
```